K7 Teardown looking for leading edge design not typical for our industry

We need to incorporate our new company tag line "foundations, follow-through, fairness" into our cards. Im open to any type of design for this and colour treatment. In fact the whole card needs a new lay out including the back. "Sustainable Deconstruction" needs to be removed from the back and the new tagline used. Would like to see different text and treatment used for "Deconstruction & Demolition".

Target Market(s)

Construction

Industry/Entity Type

Construction Company

Contact Information for Business Card

Standard business card size

Font styles to use
Sans Serif

Colors
9bcb3c
0255a3
f37122

Requirements
Should not have
• Irregular sizing.

```html
<!DOCTYPE html>
<html lang="en">
<head>
<meta charset="utf-8">
<title>K7 Teardown — Business Cards</title>
<link href="https://fonts.googleapis.com/css2?family=Montserrat:wght@500;700;800&family=Questrial&display=swap" rel="stylesheet">
<style>
  :root {
    --green: #9bcb3c;
    --blue: #0255a3;
    --orange: #f37122;
    --teal: #0f6b6e;
    --ink: #1d1d1d;
    --paper: #ffffff;
    --backdrop: #ece8e1;
  }
  * { margin: 0; padding: 0; box-sizing: border-box; }
  html, body { width: 1200px; height: 892px; overflow: hidden; }
  body {
    background: var(--backdrop);
    position: relative;
    font-family: "Montserrat", sans-serif;
  }
  .card {
    position: absolute;
    background: var(--paper);
    overflow: hidden;
    box-shadow: 0 6px 18px rgba(0,0,0,.18);
  }

  /* Back of card */
  .card-back { left: 580px; top: 60px; width: 560px; height: 320px; }
  .card-back svg { display: block; }
  .back-name {
    font-family: "Montserrat", sans-serif;
    font-weight: 800;
    fill: var(--teal);
  }
  .back-tagline {
    font-family: "Questrial", sans-serif;
    font-size: 16px;
    fill: var(--teal);
    letter-spacing: .4px;
  }

  /* Front of card */
  .card-front { left: 60px; top: 430px; width: 680px; height: 389px; }
  .band-top {
    position: absolute; left: 0; top: 0; width: 100%; height: 26px;
    background: var(--orange);
  }
  .band-bottom {
    position: absolute; left: 0; bottom: 0; width: 100%; height: 46px;
    background: var(--blue);
  }
  .brand {
    position: absolute; left: 34px; top: 62px; width: 250px;
    display: flex; align-items: center; gap: 12px;
  }
  .brand-dot {
    width: 30px; height: 30px; border-radius: 50%;
    background: var(--green); flex: none;
  }
  .brand-name {
    font-weight: 800; font-size: 34px; line-height: 1;
    color: var(--teal); letter-spacing: -.5px;
  }
  .company-line {
    position: absolute; left: 34px; top: 190px;
    font-weight: 700; font-size: 25px; line-height: 1.12;
    color: var(--teal); text-transform: uppercase; letter-spacing: .3px;
  }

  .person { position: absolute; left: 330px; top: 46px; width: 320px; text-align: center; }
  .person-name {
    font-family: "Questrial", sans-serif; font-size: 36px;
    color: var(--teal); letter-spacing: 1.5px; line-height: 1;
  }
  .person-title {
    font-family: "Questrial", sans-serif; font-size: 15px;
    color: var(--green); margin-top: 4px;
  }

  .contacts {
    position: absolute; left: 320px; top: 118px; width: 340px;
    display: grid; grid-template-columns: 1fr 1fr; row-gap: 8px; column-gap: 10px;
    font-family: "Questrial", sans-serif; font-size: 15px; color: var(--ink);
  }
  .contact { display: flex; align-items: center; gap: 7px; white-space: nowrap; }
  .contact svg { flex: none; }
  .contact-fax {
    grid-column: 1 / -1; flex-direction: column; gap: 4px; margin-top: 4px;
  }

  .address {
    position: absolute; left: 330px; top: 232px; width: 320px; text-align: center;
    font-family: "Questrial", sans-serif; font-size: 16px; color: var(--ink); line-height: 1.3;
  }
  .address-mark { display: flex; align-items: center; justify-content: center; gap: 14px; margin-bottom: 6px; }
  .flourish { width: 54px; height: 3px; border-radius: 2px; background: var(--green); }
</style>
</head>
<body>

  <!-- Back of card -->
  <div class="card card-back">
    <svg width="560" height="320" viewBox="0 0 560 320" aria-label="Card back with diagonal brand stripes and tagline">
      <g transform="rotate(40 280 160)">
        <rect x="-300" y="48"  width="1160" height="50" fill="var(--orange)"/>
        <rect x="-300" y="108" width="1160" height="46" fill="var(--blue)"/>
        <rect x="-300" y="164" width="1160" height="52" fill="var(--green)"/>
      </g>
      <circle cx="300" cy="150" r="92" fill="var(--paper)"/>
      <text class="back-name" x="300" y="144" font-size="30" text-anchor="middle">K7</text>
      <text class="back-name" x="300" y="176" font-size="30" text-anchor="middle">Teardown</text>
      <text class="back-tagline" x="30" y="294">foundations, follow-through, fairness</text>
    </svg>
  </div>

  <!-- Front of card -->
  <div class="card card-front">
    <div class="band-top"></div>

    <div class="brand">
      <span class="brand-dot"></span>
      <span class="brand-name">K7 Teardown</span>
    </div>

    <p class="company-line">Teardown<br>&amp; Demolition Inc.</p>

    <div class="person">
      <p class="person-name">Marcus Hale</p>
      <p class="person-title">Head Estimator</p>
    </div>

    <div class="contacts">
      <div class="contact">
        <svg width="16" height="16" viewBox="0 0 16 16" aria-hidden="true"><circle cx="8" cy="8" r="7" fill="none" stroke="var(--ink)" stroke-width="1.2"/><path d="M5.3 4.5l1.3-.4.8 1.7-.8.7a5 5 0 0 0 2 2l.7-.8 1.7.8-.4 1.3c-2.8.3-5.6-2.5-5.3-5.3z" fill="var(--ink)"/></svg>
        <span>(587) 555.0142</span>
      </div>
      <div class="contact">
        <svg width="16" height="16" viewBox="0 0 16 16" aria-hidden="true"><circle cx="8" cy="8" r="7" fill="none" stroke="var(--ink)" stroke-width="1.2"/><circle cx="8" cy="8" r="3.6" fill="none" stroke="var(--ink)" stroke-width="1"/><path d="M4.4 8h7.2M8 4.4v7.2" stroke="var(--ink)" stroke-width=".8"/></svg>
        <span>marcush@k7teardown.com</span>
      </div>
      <div class="contact">
        <svg width="16" height="16" viewBox="0 0 16 16" aria-hidden="true"><circle cx="8" cy="8" r="7" fill="none" stroke="var(--ink)" stroke-width="1.2"/><rect x="5.8" y="4" width="4.4" height="8" rx=".8" fill="none" stroke="var(--ink)" stroke-width="1"/></svg>
        <span>(780) 555-0178</span>
      </div>
      <div class="contact">
        <svg width="16" height="16" viewBox="0 0 16 16" aria-hidden="true"><circle cx="8" cy="8" r="7" fill="none" stroke="var(--ink)" stroke-width="1.2"/><rect x="4.3" y="5.3" width="7.4" height="5.4" fill="var(--ink)"/><path d="M4.3 5.3l3.7 3 3.7-3" fill="none" stroke="var(--paper)" stroke-width=".8"/></svg>
        <span>www.k7teardown.com</span>
      </div>
      <div class="contact contact-fax">
        <svg width="16" height="16" viewBox="0 0 16 16" aria-hidden="true"><circle cx="8" cy="8" r="7" fill="none" stroke="var(--ink)" stroke-width="1.2"/><rect x="4.2" y="6.5" width="7.6" height="4" rx=".6" fill="var(--ink)"/><rect x="5.6" y="4.3" width="4.8" height="2.4" fill="var(--ink)"/></svg>
        <span>(780) 555-0193</span>
      </div>
    </div>

    <div class="address">
      <div class="address-mark">
        <span class="flourish" role="img" aria-label="Small decorative flourish"></span>
        <svg width="18" height="18" viewBox="0 0 16 16" aria-hidden="true"><circle cx="8" cy="8" r="7" fill="none" stroke="var(--ink)" stroke-width="1.2"/><path d="M8 12.4S5.2 9.2 5.2 7.2a2.8 2.8 0 0 1 5.6 0c0 2-2.8 5.2-2.8 5.2z" fill="var(--ink)"/><circle cx="8" cy="7.2" r="1" fill="var(--paper)"/></svg>
        <span class="flourish" role="img" aria-label="Small decorative flourish"></span>
      </div>
      <p>#210, 4470 - 96 Street<br>Riverton, AB T9X 4K2</p>
    </div>

    <div class="band-bottom"></div>
  </div>

</body>
</html>
```